New Brochure Design Project - downloadable PDF

Capability Statement, Brochure and Website - we are looking for a uniform of the three marketing assets that deliver a professional look and feel for executive-level decision-makers. Our company provides guest and patient-facing technologies. For the most part, the technologies are: smart TVs, Wi-Fi, RTLS, Integrated services. I have submitted the editable files we have, but in terms of industry images, we are happy to have others recommended. I have also submitted previous efforts and one Capability Statement from a company (KMB) that is well received.
Updates
Need extra days to review
Target Market(s)
Corporate and Government Procurement (Healthtcare and Hotels/Resorts)
Industry/Entity Type
Healthcare and Hotel/Resorts
Look and feel

```html
<!DOCTYPE html>
<html lang="en">
<head>
<meta charset="utf-8">
<title>Brightward Brochure – Company Overview Spread</title>
<link href="https://fonts.googleapis.com/css2?family=Poppins:wght@400;500;700;800&display=swap" rel="stylesheet">
<style>
  :root {
    --canvas: #d6d6d6;
    --paper: #ffffff;
    --ink: #1c1c1c;
    --muted: #3a3a3a;
    --accent: #e10f12;
    --rule: #e2e2e2;
    --map-dark: #1e1e1e;
    --map-mid: #6b6b6b;
    --photo-light: #f1efec;
    --photo-mid: #bdb8b0;
    --photo-dark: #5d6a57;
  }
  * { margin: 0; padding: 0; box-sizing: border-box; }
  html, body {
    width: 970px; height: 1200px; overflow: hidden;
    background: var(--canvas);
    font-family: "Poppins", sans-serif;
    color: var(--ink);
  }
  .spread {
    position: absolute;
    left: 20px; top: 436px;
    width: 930px; height: 328px;
    display: flex;
    box-shadow: 0 6px 14px rgba(0,0,0,0.25);
  }
  .page {
    position: relative;
    width: 465px; height: 328px;
    background: var(--paper);
    overflow: hidden;
  }
  .page-title {
    position: absolute;
    left: 23px; top: 20px;
    font-size: 20px; line-height: 1;
    font-weight: 400;
    letter-spacing: -0.2px;
  }
  .page-title .highlight, .section-title {
    color: var(--accent);
    font-weight: 800;
  }
  .body-copy {
    font-size: 6.6px;
    line-height: 1.35;
    color: var(--muted);
  }
  .body-copy p + p { margin-top: 3px; }
  .overview-copy {
    position: absolute;
    left: 23px; top: 52px;
    width: 390px;
  }
  .world-map {
    position: absolute;
    left: 46px; top: 104px;
    width: 330px; height: 190px;
    border-radius: 40px 70px 60px 30px;
    background:
      radial-gradient(ellipse at 25% 35%, var(--map-dark) 0 30%, transparent 60%),
      radial-gradient(ellipse at 65% 30%, var(--map-dark) 0 35%, transparent 62%),
      radial-gradient(ellipse at 85% 80%, var(--map-mid) 0 20%, transparent 45%),
      linear-gradient(160deg, #4a4a4a, #9a9a9a);
    opacity: 0.85;
  }
  .map-pin { position: absolute; width: 11px; height: 16px; }
  .page-footer {
    position: absolute;
    left: 23px; right: 23px; bottom: 16px;
    display: flex; justify-content: space-between;
    font-size: 5.4px;
  }
  .site-url { letter-spacing: 1.2px; color: var(--muted); }
  .page-number { font-weight: 700; }
  .page-number span { color: var(--accent); }
  .accent-bar {
    position: absolute;
    left: 0; bottom: 0;
    width: 378px; height: 3px;
    background: var(--accent);
    border-top-right-radius: 3px;
  }
  .section-title {
    position: absolute;
    left: 23px;
    font-size: 18px; line-height: 1;
  }
  .profile-title { top: 20px; }
  .profile-copy { position: absolute; left: 23px; top: 52px; width: 188px; }
  .section-rule {
    position: absolute;
    left: 23px; top: 155px;
    width: 188px; height: 1px;
    background: var(--rule);
  }
  .vision-title { top: 175px; }
  .vision-copy { position: absolute; left: 23px; top: 207px; width: 188px; }
  .workspace-photo {
    position: absolute;
    right: 0; top: 0;
    width: 265px; height: 328px;
    background:
      linear-gradient(90deg, var(--paper) 0%, rgba(255,255,255,0) 30%),
      radial-gradient(ellipse at 55% 38%, var(--photo-dark) 0 14%, transparent 32%),
      radial-gradient(ellipse at 90% 12%, #7d8a6e 0 12%, transparent 30%),
      radial-gradient(ellipse at 60% 55%, var(--photo-mid) 0 22%, transparent 48%),
      linear-gradient(160deg, var(--photo-light), #e3dfd9);
  }
  .page-right .page-footer { right: 23px; }
  .page-right .page-number { color: var(--ink); }
</style>
</head>
<body>
  <main class="spread">
    <section class="page page-left">
      <h1 class="page-title">Company <span class="highlight">Overview</span></h1>
      <div class="body-copy overview-copy">
        <p>Brightward Pty Ltd is a nonlisted public company that provides IoT solutions, technical services, entertainment and communication to hotels, healthcare, aged care, mining camps and education facilities.</p>
        <p>BWD operates offices in Australia, New Zealand and the United States of America.</p>
      </div>
      <div class="world-map" role="img" aria-label="Black watercolour world map"></div>
      <svg class="map-pin" style="left:97px;top:150px" viewBox="0 0 12 18" aria-hidden="true"><path d="M6 0a6 6 0 0 0-6 6c0 4.5 6 12 6 12s6-7.5 6-12a6 6 0 0 0-6-6z" fill="#e10f12"/><circle cx="6" cy="6" r="2.3" fill="#fff"/></svg>
      <svg class="map-pin" style="left:251px;top:175px" viewBox="0 0 12 18" aria-hidden="true"><path d="M6 0a6 6 0 0 0-6 6c0 4.5 6 12 6 12s6-7.5 6-12a6 6 0 0 0-6-6z" fill="#e10f12"/><circle cx="6" cy="6" r="2.3" fill="#fff"/></svg>
      <svg class="map-pin" style="left:291px;top:215px" viewBox="0 0 12 18" aria-hidden="true"><path d="M6 0a6 6 0 0 0-6 6c0 4.5 6 12 6 12s6-7.5 6-12a6 6 0 0 0-6-6z" fill="#e10f12"/><circle cx="6" cy="6" r="2.3" fill="#fff"/></svg>
      <svg class="map-pin" style="left:310px;top:232px" viewBox="0 0 12 18" aria-hidden="true"><path d="M6 0a6 6 0 0 0-6 6c0 4.5 6 12 6 12s6-7.5 6-12a6 6 0 0 0-6-6z" fill="#e10f12"/><circle cx="6" cy="6" r="2.3" fill="#fff"/></svg>
      <footer class="page-footer">
        <span class="site-url">www.brightward.com</span>
        <span class="page-number">Pg <span>1</span></span>
      </footer>
      <div class="accent-bar"></div>
    </section>

    <section class="page page-right">
      <div class="workspace-photo" role="img" aria-label="Photo of hands working on a laptop showing a hotel welcome screen, with coffee cup, glasses and plant on a white desk"></div>
      <h2 class="section-title profile-title">Profile</h2>
      <div class="body-copy profile-copy">
        <p>With extensive industry experience and over 10,000 endpoints across Australia, New Zealand, Fiji, Indonesia, Singapore and United States of America – Brightward (BWD) is able to bring together the best outcomes for your facility.</p>
        <p>BWD was founded in 2008 to capitalize on the anticipated growth in on-demand Wi-Fi, Information and Content for Hotels</p>
      </div>
      <div class="section-rule"></div>
      <h2 class="section-title vision-title">Vision</h2>
      <div class="body-copy vision-copy">
        <p>To be the first choice and solution provider through dynamic and flexible integration platforms, extending to hospitals, aged care facilities, student, regional and remote accommodation facilities, and mining camps.</p>
      </div>
      <footer class="page-footer">
        <span class="site-url">www.brightward.com</span>
        <span class="page-number">Pg <span>2</span></span>
      </footer>
      <div class="accent-bar"></div>
    </section>
  </main>
</body>
</html>
```